Brenvik Innovations
Professional
Daniel Marlow
CEO
5812-4 Calloway Ave #2267
Houston, TX 77194
Daniel@BrenvikInnovations.com
BrenvikInnovations.com
Feel free to play with the function of the business card if possible as seen in: http://www.trelvaform-studio.com/blog/wp-content/uploads/2009/12/lock-picking-business-card.jpg. Card can be paper plastic or metal.
Our company specializes in artificial intelligence, Unmanned aerial vehicles human-machine interfaces and lasers. Please keep this in mind in your designs.
surprise me, I will refine my requirement here after I see a few submissions.
Here are the business logo files

```html
<!DOCTYPE html>
<html lang="en">
<head>
<meta charset="utf-8">
<title>Brenvik Innovations – Business Card</title>
<link href="https://fonts.googleapis.com/css2?family=Exo+2:wght@600&display=swap" rel="stylesheet">
<style>
  :root {
    --page-bg: #eef0f4;
    --card-base: #3c3c3c;
    --card-band-inner: #454545;
    --card-band-outer: #505050;
    --brand-white: #f4f4f4;
  }
  html, body {
    margin: 0;
    padding: 0;
    width: 1200px;
    height: 878px;
    overflow: hidden;
    background: var(--page-bg);
  }
  .canvas {
    position: relative;
    width: 1200px;
    height: 878px;
  }
  .business-card {
    position: absolute;
    left: 220px;
    top: 224px;
    width: 760px;
    height: 430px;
    filter: drop-shadow(0 10px 24px rgba(0,0,0,0.18));
  }
  .card-shape {
    position: absolute;
    inset: 0;
    width: 760px;
    height: 430px;
  }
  .brand-lockup {
    position: absolute;
    left: 70px;
    top: 0;
    height: 430px;
    display: flex;
    align-items: center;
    gap: 26px;
  }
  .brand-mark {
    width: 64px;
    height: 64px;
    border-radius: 50%;
    background: var(--brand-white);
    flex: none;
  }
  .brand-name {
    font-family: "Exo 2", sans-serif;
    font-weight: 600;
    font-size: 48px;
    letter-spacing: 2px;
    text-transform: uppercase;
    color: var(--brand-white);
    line-height: 1;
  }
</style>
</head>
<body>
  <main class="canvas">
    <section class="business-card" aria-label="Brenvik Innovations business card, back side">
      <svg class="card-shape" viewBox="0 0 760 430" xmlns="http://www.w3.org/2000/svg" aria-hidden="true">
        <defs>
          <clipPath id="card-outline">
            <path d="M30,0 H730 L760,30 V400 L730,430 H30 L0,400 V30 Z"/>
          </clipPath>
        </defs>
        <g clip-path="url(#card-outline)">
          <rect width="760" height="430" fill="var(--card-base)"/>
          <path d="M500,0 Q720,190 600,430 H760 V0 Z" fill="var(--card-band-inner)"/>
          <path d="M610,0 Q790,200 690,430 H760 V0 Z" fill="var(--card-band-outer)"/>
        </g>
      </svg>
      <div class="brand-lockup">
        <span class="brand-mark" aria-hidden="true"></span>
        <span class="brand-name">Brenvik Innovations</span>
      </div>
    </section>
  </main>
</body>
</html>
```